Business Card Design Project - Brindle Media

We need a new business card that fits with our new logo. We are a social media agency and consultancy operating in China. We want a fresh and strong business card. Our cards need to be two-sided as we have both English and Chinese language names and addresses on the card, but as with our current business card this does not need to be a mirror-image. Our thoughts go out to a white card on the front where the logo/name is and then using the logo colours for different coloured back-grounds. i.e that the back of the biz card works with the four different colours in the logo.

Attached is the new logo, and also a copy of our old business cards.

Target Market(s)

CEO's, CMO's. media and advertising professionals

Industry/Entity Type

Business

Requirements
Must have
• inclusion of both Chinese and English language
Nice to have
• four different colored versions of the back of the biz card. Our logo has four colors and each of these colors we would like to have a version of.

```html
<!DOCTYPE html>
<html lang="en">
<head>
<meta charset="utf-8">
<title>Brindle Media – Business Card Backs</title>
<link rel="stylesheet" href="https://fonts.googleapis.com/css2?family=Comfortaa:wght@700&family=Michroma&family=Noto+Sans+SC:wght@500&display=swap">
<style>
  :root {
    --paper: #ffffff;
    --ink: #1c1c1c;
    --orange: #ff4713;
    --violet: #3d14f2;
    --magenta: #ff14ee;
    --lime: #86ff0f;
    --card-w: 596px;
    --card-h: 356px;
  }
  html, body {
    margin: 0;
    padding: 0;
    width: 1200px;
    height: 900px;
    overflow: hidden;
    background: var(--paper);
  }
  .sheet {
    position: relative;
    width: 1200px;
    height: 900px;
  }
  .card {
    position: absolute;
    width: var(--card-w);
    height: var(--card-h);
    background: var(--paper);
    overflow: hidden;
  }
  .card--orange  { left: 0;     top: 0;     --accent: var(--orange); }
  .card--violet  { left: 604px; top: 0;     --accent: var(--violet); }
  .card--magenta { left: 0;     top: 382px; --accent: var(--magenta); }
  .card--lime    { left: 604px; top: 382px; --accent: var(--lime); }

  .card__art {
    position: absolute;
    inset: 0;
    width: 100%;
    height: 100%;
  }
  .card__panel { fill: var(--accent); }

  .wordmark {
    position: absolute;
    left: 88px;
    top: 46px;
    font-family: "Comfortaa", sans-serif;
    font-weight: 700;
    color: var(--ink);
    line-height: 1;
    text-align: right;
  }
  .wordmark__name {
    display: block;
    font-size: 54px;
    letter-spacing: -1px;
  }
  .wordmark__sub {
    display: block;
    font-size: 20px;
    margin-top: 2px;
  }

  .card__details {
    position: absolute;
    left: 438px;
    top: 192px;
    margin: 0;
    font-family: "Michroma", "Noto Sans SC", sans-serif;
    font-size: 9px;
    line-height: 16px;
    color: var(--ink);
    white-space: nowrap;
  }
  .card__details span { display: block; }
  .card--violet .card__details .is-light { color: var(--paper); }

  .card__tagline {
    position: absolute;
    left: 124px;
    top: 306px;
    margin: 0;
    font-family: "Noto Sans SC", sans-serif;
    font-weight: 500;
    font-size: 11px;
    line-height: 16px;
    color: var(--ink);
    white-space: nowrap;
  }
</style>
</head>
<body>
<main class="sheet">

  <section class="card card--orange" aria-label="Card back, orange">
    <svg class="card__art" viewBox="0 0 298 178" preserveAspectRatio="none" aria-hidden="true">
      <defs>
        <linearGradient id="swoosh-a" x1="0" y1="0" x2="1" y2="0">
          <stop offset="0" stop-color="#e6e6e6" stop-opacity="0.2"/>
          <stop offset="0.5" stop-color="#d4d4d4"/>
          <stop offset="1" stop-color="#e6e6e6" stop-opacity="0"/>
        </linearGradient>
      </defs>
      <path d="M0,72 C45,98 120,100 188,84 C130,104 60,110 0,96 Z" fill="url(#swoosh-a)"/>
      <path class="card__panel" d="M184,0 C202,30 200,58 180,90 C164,116 157,146 158,178 L298,178 L298,0 Z"/>
    </svg>
    <div class="wordmark"><span class="wordmark__name">brindle</span><span class="wordmark__sub">media</span></div>
    <p class="card__details"><span>Lena Wu 吴丽娜</span><span>+86 21 5550 0188</span><span>lena@brindle.cn</span></p>
    <p class="card__tagline">博林德传媒 · 上海</p>
  </section>

  <section class="card card--violet" aria-label="Card back, violet">
    <svg class="card__art" viewBox="0 0 298 178" preserveAspectRatio="none" aria-hidden="true">
      <path d="M0,72 C45,98 120,100 188,84 C130,104 60,110 0,96 Z" fill="url(#swoosh-a)"/>
      <path class="card__panel" d="M184,0 C202,30 200,58 180,90 C164,116 157,146 158,178 L298,178 L298,0 Z"/>
    </svg>
    <div class="wordmark"><span class="wordmark__name">brindle</span><span class="wordmark__sub">media</span></div>
    <p class="card__details"><span>Lena Wu 吴丽娜</span><span class="is-light">+86 21 5550 0188</span><span>lena@brindle.cn</span></p>
    <p class="card__tagline">博林德传媒 · 上海</p>
  </section>

  <section class="card card--magenta" aria-label="Card back, magenta">
    <svg class="card__art" viewBox="0 0 298 178" preserveAspectRatio="none" aria-hidden="true">
      <path d="M0,72 C45,98 120,100 188,84 C130,104 60,110 0,96 Z" fill="url(#swoosh-a)"/>
      <path class="card__panel" d="M184,0 C202,30 200,58 180,90 C164,116 157,146 158,178 L298,178 L298,0 Z"/>
    </svg>
    <div class="wordmark"><span class="wordmark__name">brindle</span><span class="wordmark__sub">media</span></div>
    <p class="card__details"><span>Lena Wu 吴丽娜</span><span>+86 21 5550 0188</span><span>lena@brindle.cn</span></p>
    <p class="card__tagline">博林德传媒 · 上海</p>
  </section>

  <section class="card card--lime" aria-label="Card back, lime">
    <svg class="card__art" viewBox="0 0 298 178" preserveAspectRatio="none" aria-hidden="true">
      <path d="M0,72 C45,98 120,100 188,84 C130,104 60,110 0,96 Z" fill="url(#swoosh-a)"/>
      <path class="card__panel" d="M184,0 C202,30 200,58 180,90 C164,116 157,146 158,178 L298,178 L298,0 Z"/>
    </svg>
    <div class="wordmark"><span class="wordmark__name">brindle</span><span class="wordmark__sub">media</span></div>
    <p class="card__details"><span>Lena Wu 吴丽娜</span><span>+86 21 5550 0188</span><span>lena@brindle.cn</span></p>
    <p class="card__tagline">博林德传媒 · 上海</p>
  </section>

</main>
</body>
</html>
```